cool postcard design wanted 1 sided

need the back side of a postcard redone to be professional and catchy looking. same info wanted that is on demo flyer attached. current size is 4x6 but would want psd file so i can resize and save easily within a few inches. would like photo of woman to be prominent. s a design that will really catch attention and ok if a bit playful

Target Market(s)

to get real estate listings, people who want to sell their home

Industry/Entity Type

Real Estate Agent

Colors

Designer to choose colors to be used in the design.

Requirements
Must have
• picture of lady prominent easy to read font throughout
Nice to have
• clean professional and eye catching
Should not have
• clutter

```html
<!DOCTYPE html>
<html lang="en">
<head>
<meta charset="utf-8">
<title>Marisol Vega Realtor Postcard</title>
<link rel="stylesheet" href="https://fonts.googleapis.com/css2?family=Oswald:wght@300;500;700&family=Roboto:wght@400;700&display=swap">
<style>
  :root {
    --page: #ececec;
    --red: #8e1418;
    --red-deep: #5a0a0d;
    --red-bright: #d3242a;
    --black: #111111;
    --white: #ffffff;
    --ink: #333333;
    --green: #4a8a2a;
    --stamp: #d8d8d8;
  }
  * { margin: 0; padding: 0; box-sizing: border-box; }
  html, body { width: 1200px; height: 900px; overflow: hidden; background: var(--page); }
  .postcard {
    position: absolute; left: 60px; top: 90px; width: 1080px; height: 720px;
    background: var(--white); overflow: hidden;
    box-shadow: 0 6px 18px rgba(0,0,0,.18);
    font-family: "Roboto", Arial, sans-serif;
  }
  .postcard__shapes { position: absolute; inset: 0; }
  .headline {
    position: absolute; left: 34px; top: 26px; width: 470px;
    font-family: "Oswald", sans-serif; color: var(--white); text-transform: uppercase;
  }
  .headline__lead { font-weight: 300; font-size: 36px; line-height: 1.1; }
  .headline__main { font-weight: 700; font-size: 54px; line-height: 1.05; }
  .headline__cta { font-weight: 700; font-size: 36px; text-align: right; line-height: 1.1; }
  .agent-photo { position: absolute; left: 24px; top: 190px; width: 290px; height: 370px; display: block; }
  .sale-sign { position: absolute; left: 336px; top: 196px; width: 180px; height: 364px; display: block; }
  .contact {
    position: absolute; left: 24px; top: 572px; width: 520px;
    font-family: "Oswald", sans-serif; color: var(--white);
  }
  .contact__quote { font-weight: 700; font-size: 32px; color: var(--red-bright); line-height: 1.15; }
  .contact__quote-mark { color: var(--white); }
  .contact__phone { font-weight: 700; font-size: 44px; line-height: 1.15; }
  .contact__tagline { font-weight: 500; font-size: 22px; text-transform: uppercase; }
  .return-address {
    position: absolute; left: 640px; top: 40px; font-style: normal;
    font-size: 17px; line-height: 1.3; color: var(--ink); text-transform: uppercase;
  }
  .stamp { position: absolute; right: 40px; top: 36px; width: 110px; height: 110px; background: var(--stamp); }
  .address-box {
    position: absolute; left: 700px; top: 250px; width: 220px; height: 110px;
    border: 2px solid var(--ink); padding: 22px 18px; font-size: 17px; line-height: 1.5; color: var(--ink);
  }
  .brand { position: absolute; left: 730px; top: 410px; display: flex; align-items: center; gap: 12px; }
  .brand__dot { width: 26px; height: 26px; border-radius: 50%; background: var(--green); }
  .brand__name { font-family: "Oswald", sans-serif; font-weight: 500; font-size: 30px; color: var(--green); }
  .badges { position: absolute; left: 790px; top: 480px; display: flex; gap: 24px; }
  .badge { width: 44px; height: 44px; background: var(--black); }
  .website {
    position: absolute; left: 600px; top: 598px; width: 460px; text-align: center;
    font-family: "Oswald", sans-serif; font-weight: 700; font-size: 38px; line-height: 1.2; color: var(--red);
  }
  .disclaimer {
    position: absolute; left: 600px; top: 652px; width: 460px; text-align: center;
    font-size: 12px; color: var(--ink); text-transform: uppercase;
  }
</style>
</head>
<body>
  <article class="postcard">
    <svg class="postcard__shapes" width="1080" height="720" viewBox="0 0 1080 720">
      <defs>
        <linearGradient id="panelRed" x1="0" y1="0" x2="1" y2="1">
          <stop offset="0" stop-color="#a5191e"/>
          <stop offset="1" stop-color="#5a0a0d"/>
        </linearGradient>
      </defs>
      <path class="swoosh-edge" d="M0 0 H540 C620 130 640 300 590 450 C555 560 520 640 600 720 H0 Z" fill="var(--black)"/>
      <path class="panel" d="M0 0 H505 C585 130 605 300 555 450 C530 530 515 560 520 560 H0 Z" fill="url(#panelRed)"/>
    </svg>

    <header class="headline">
      <p class="headline__lead">Thinking of buying or</p>
      <h1 class="headline__main">Selling a home?</h1>
      <p class="headline__cta">Lets talk</p>
    </header>

    <svg class="agent-photo" role="img" aria-label="Portrait photo of the realtor, smiling, in a white blouse" viewBox="0 0 290 370">
      <defs>
        <linearGradient id="photoTone" x1="0" y1="0" x2="0" y2="1">
          <stop offset="0" stop-color="#7a2418"/>
          <stop offset="0.45" stop-color="#a8705a"/>
          <stop offset="1" stop-color="#efe9e4"/>
        </linearGradient>
      </defs>
      <rect width="290" height="370" fill="url(#photoTone)"/>
    </svg>

    <svg class="sale-sign" role="img" aria-label="Illustration of a white post with a red For Sale sign" viewBox="0 0 180 364">
      <defs>
        <linearGradient id="signTone" x1="0" y1="0" x2="0" y2="1">
          <stop offset="0" stop-color="#e9e4e4"/>
          <stop offset="0.5" stop-color="#c9383c"/>
          <stop offset="1" stop-color="#9a1a1e"/>
        </linearGradient>
      </defs>
      <rect width="180" height="364" fill="url(#signTone)"/>
    </svg>

    <section class="contact">
      <p class="contact__quote"><span class="contact__quote-mark">“</span> I would love to be your realtor <span class="contact__quote-mark">”</span></p>
      <p class="contact__phone">(555) 214-7730</p>
      <p class="contact__tagline">Friendly &amp; professional realtor services</p>
    </section>

    <address class="return-address">
      Return Address<br>
      1280 Maple Crest Dr Suite 310<br>
      Fairview, TX 75000
    </address>
    <div class="stamp"></div>

    <div class="address-box">Local<br>Poster Customer</div>

    <div class="brand">
      <span class="brand__dot"></span>
      <span class="brand__name">Birch Hollow Realty</span>
    </div>
    <div class="badges">
      <span class="badge"></span>
      <span class="badge"></span>
    </div>

    <p class="website">MARISOLVEGAREALTOR.COM</p>
    <p class="disclaimer">This is not a solicitation if you already have representation</p>
  </article>
</body>
</html>
```